Off Grid consulting and outdoor products needs a website

We need a website design to help launch our new business. Its a business that plans to offer Off-grid conslting and outdoor survival products to people who are looking to relocate or vacation to properties/homes that are Off-grid. We plan to offer design plans for homes/cabins, renewable energy systems for power/heating etc, survival products for outdoor vacations/living. We also do consulting and project management for those who want to design and build from scratch their dream off-grid home or vacation property. I've included our logo design for use.
Would like the website to include 5 pages.
www.ridgepinehaven.com
The main landing page (1)
want a video loop backround with a flyover of a cabin in the woods.
https://www.clipvaultora.com/video/clip-48291736-blue-sky-melting-snow-on-green-energy
(also need a backup static image of just high-shot of cabin in woods)
logo top left, Quoted string of text in the middle, over the video. and a CTA button to 'Contact us'
picture links below that to last 3 recent blog posts.
About Us page (2)
(example) https://larkwildgear.com/pages/about-lark
Blog page (3)
blog posts associated with pictures.
Consulting 'services' page (4)
-land services and moving off-grid
-Building off grid
-Renewable energy off-grid
-Sustainable farming and all season greenhouses
Store page 'comming soon' (5)
(Example) http://timberly.crestlayouts.com/demo-1/demo.html

Target Market(s)

Outdoor enthusiasts and people who want to escape their city life

Coding

Coded - Design and coding required

Requirements
Must have
• Outdoor feel, woods, cabin, reneable energy (solar, geothermal, greenhouses, water wells)

```html
<!DOCTYPE html>
<html lang="en">
<head>
<meta charset="utf-8">
<title>Ridgepine Haven — Blog</title>
<link href="https://fonts.googleapis.com/css2?family=Oswald:wght@500;700&family=Poppins:wght@400;500;600;700&display=swap" rel="stylesheet">
<style>
:root{
  --ink:#1b1b1b;
  --muted:#6a6a6a;
  --line:#dcdcdc;
  --panel:#f3f3f3;
  --white:#ffffff;
  --footer:#121413;
  --forest-light:#b9c4be;
  --forest-mid:#3f5a4a;
  --forest-dark:#17241d;
  --accent:#1b1b1b;
}
*{box-sizing:border-box;margin:0;padding:0}
html,body{width:1200px;height:2464px;overflow:hidden}
body{position:relative;background:var(--white);font-family:'Poppins',sans-serif;color:var(--ink)}
.abs{position:absolute}

/* header */
.site-header{left:0;top:0;width:1200px;height:96px;background:var(--white)}
.brand{left:40px;top:18px;display:flex;align-items:center;gap:10px;font-family:'Oswald',sans-serif;font-weight:700;font-size:26px;letter-spacing:1px;color:var(--ink);text-transform:uppercase}
.brand-mark{width:34px;height:34px;background:var(--ink)}
.main-nav{right:40px;top:34px;display:flex;gap:26px;font-family:'Oswald',sans-serif;font-weight:500;font-size:15px;letter-spacing:.5px}
.main-nav a{color:var(--ink);text-decoration:none}
.main-nav .active{color:#8a8a8a}

.page-title{left:0;top:148px;width:1200px;text-align:center;font-family:'Oswald',sans-serif;font-weight:700;font-size:58px;letter-spacing:1px}

/* backdrop */
.forest-backdrop{left:0;top:1420px;width:1200px;height:740px;background:linear-gradient(180deg,var(--white) 0%,var(--forest-light) 30%,var(--forest-mid) 65%,var(--forest-dark) 100%)}
.content-panel{left:80px;top:262px;width:1040px;height:1460px;background:linear-gradient(180deg,var(--panel) 85%,rgba(243,243,243,0) 100%)}

/* cards */
.post-card{width:350px;height:424px;background:var(--white);box-shadow:0 2px 8px rgba(0,0,0,.08)}
.post-image{width:350px;height:248px}
.post-body{padding:20px 22px}
.post-title{font-family:'Poppins',sans-serif;font-weight:700;font-size:15px;text-transform:uppercase;margin-bottom:8px}
.post-excerpt{font-size:12px;line-height:18px;color:var(--muted);margin-bottom:18px}
.read-more{font-size:10px;font-weight:600;color:var(--ink);text-decoration:underline;text-transform:uppercase}

/* pagination */
.pagination{left:280px;top:1660px;display:flex;gap:10px;align-items:center;font-size:12px}
.page-btn{height:30px;min-width:30px;padding:0 10px;display:flex;align-items:center;justify-content:center;border:1px solid var(--line);background:var(--white);border-radius:3px}
.page-num{min-width:22px;text-align:center}
.page-num.current{width:30px;height:30px;border-radius:50%;background:var(--accent);color:var(--white);display:flex;align-items:center;justify-content:center}

/* sidebar */
.sidebar{left:880px;top:284px;width:230px}
.side-label{font-family:'Oswald',sans-serif;font-weight:700;font-size:14px;text-transform:uppercase;margin-bottom:8px}
.search-box{height:32px;border:1px solid var(--line);background:var(--white);display:flex;align-items:center;justify-content:space-between;padding:0 10px;font-size:11px;color:#9a9a9a;margin-bottom:34px}
.category-list{list-style:none;margin-bottom:30px}
.category-list li{display:flex;justify-content:space-between;font-size:12px;color:#444;padding:8px 0;border-bottom:1px solid var(--line)}
.related-item{display:flex;gap:12px;margin-bottom:16px;align-items:center}
.related-thumb{width:66px;height:66px;flex:none}
.related-date{font-size:10px;color:#999}
.related-title{font-size:12px;font-weight:700;text-transform:uppercase;line-height:16px}

/* footer */
.site-footer{left:0;top:2120px;width:1200px;height:344px;background:var(--footer);color:#e8e8e8}
.footer-brand{left:90px;top:40px;display:flex;align-items:center;gap:10px;font-family:'Oswald',sans-serif;font-weight:700;font-size:28px;text-transform:uppercase;color:var(--white)}
.footer-brand .brand-mark{background:var(--white)}
.footer-col{top:26px}
.footer-heading{font-family:'Oswald',sans-serif;font-weight:700;font-size:20px;text-transform:uppercase;margin-bottom:12px;color:var(--white)}
.footer-links{list-style:none;font-size:12px;line-height:20px}
.contact-line{display:flex;gap:8px;align-items:center;font-size:12px;line-height:22px}
.social-row{display:flex;gap:8px;margin-top:10px}
.social-dot{width:22px;height:22px;border-radius:50%;background:#3a3d3b}
.newsletter-note{font-size:11px;line-height:17px;color:#bdbdbd;margin-bottom:12px;width:240px}
.newsletter-form{display:flex;width:240px;height:32px}
.newsletter-input{flex:1;background:var(--white);color:#888;font-size:12px;display:flex;align-items:center;padding-left:10px}
.newsletter-btn{width:38px;background:#2b2e2c;display:flex;align-items:center;justify-content:center}
.copyright{left:0;top:286px;width:1200px;text-align:center;font-size:11px;color:#bdbdbd}
.to-top{left:1132px;top:264px;width:30px;height:30px;border-radius:50%;border:1px solid #666;display:flex;align-items:center;justify-content:center}
</style>
</head>
<body>

<div class="abs forest-backdrop" role="img" aria-label="Misty pine forest stretching down a valley"></div>

<header class="abs site-header">
  <div class="abs brand"><span class="brand-mark"></span>Ridgepine Haven</div>
  <nav class="abs main-nav">
    <a href="#">HOME</a><a href="#">ABOUT</a><a href="#">CONSULTING</a><a href="#" class="active">BLOG</a><a href="#">STORE</a><a href="#">CONTACT US</a>
  </nav>
</header>

<h1 class="abs page-title">BLOG POSTS ASSOCIATED</h1>

<div class="abs content-panel"></div>

<article class="abs post-card" style="left:92px;top:288px">
  <div class="post-image" role="img" aria-label="Timber frame of a cabin under construction in a field" style="background:linear-gradient(180deg,#c9cdd0,#a88e6e)"></div>
  <div class="post-body"><h2 class="post-title">Blog heading here</h2><p class="post-excerpt">Lorem ipsum is simply dummy text of the printing and typesetting industry. Lorem ipsum has been the industry's</p><a class="read-more" href="#">Read more</a></div>
</article>
<article class="abs post-card" style="left:462px;top:288px">
  <div class="post-image" role="img" aria-label="A-frame cabin among tall pine trees" style="background:linear-gradient(180deg,#6d7c70,#2f3b33)"></div>
  <div class="post-body"><h2 class="post-title">Blog heading here</h2><p class="post-excerpt">Lorem ipsum is simply dummy text of the printing and typesetting industry. Lorem ipsum has been the industry's</p><a class="read-more" href="#">Read more</a></div>
</article>
<article class="abs post-card" style="left:92px;top:736px">
  <div class="post-image" role="img" aria-label="Carpenter cutting wood in a workshop" style="background:linear-gradient(180deg,#b8ab98,#7a5a3d)"></div>
  <div class="post-body"><h2 class="post-title">Blog heading here</h2><p class="post-excerpt">Lorem ipsum is simply dummy text of the printing and typesetting industry. Lorem ipsum has been the industry's</p><a class="read-more" href="#">Read more</a></div>
</article>
<article class="abs post-card" style="left:462px;top:736px">
  <div class="post-image" role="img" aria-label="Row of A-frame timber trusses at a forest build site" style="background:linear-gradient(180deg,#9fb1a6,#7d6448)"></div>
  <div class="post-body"><h2 class="post-title">Blog heading here</h2><p class="post-excerpt">Lorem ipsum is simply dummy text of the printing and typesetting industry. Lorem ipsum has been the industry's</p><a class="read-more" href="#">Read more</a></div>
</article>
<article class="abs post-card" style="left:92px;top:1184px">
  <div class="post-image" role="img" aria-label="Cabin foundation being laid in a woodland clearing" style="background:linear-gradient(180deg,#55684f,#6b4a34)"></div>
  <div class="post-body"><h2 class="post-title">Blog heading here</h2><p class="post-excerpt">Lorem ipsum is simply dummy text of the printing and typesetting industry. Lorem ipsum has been the industry's</p><a class="read-more" href="#">Read more</a></div>
</article>
<article class="abs post-card" style="left:462px;top:1184px">
  <div class="post-image" role="img" aria-label="Handmade wooden table in a workshop" style="background:linear-gradient(180deg,#d9c4a4,#a87a4c)"></div>
  <div class="post-body"><h2 class="post-title">Blog heading here</h2><p class="post-excerpt">Lorem ipsum is simply dummy text of the printing and typesetting industry. Lorem ipsum has been the industry's</p><a class="read-more" href="#">Read more</a></div>
</article>

<nav class="abs pagination">
  <span class="page-btn">&lsaquo; Prev</span>
  <span class="page-num">1</span>
  <span class="page-num current">2</span>
  <span class="page-num">3</span>
  <span class="page-num">…</span>
  <span class="page-num">10</span>
  <span class="page-btn">Next &rsaquo;</span>
</nav>

<aside class="abs sidebar">
  <div class="side-label">Search</div>
  <div class="search-box">Search here
    <svg width="12" height="12" viewBox="0 0 12 12"><circle cx="5" cy="5" r="4" fill="none" stroke="#555" stroke-width="1.4"/><line x1="8" y1="8" x2="11" y2="11" stroke="#555" stroke-width="1.4"/></svg>
  </div>
  <div class="side-label">Categories</div>
  <ul class="category-list">
    <li>Plans for homes/cabin<span>›</span></li>
    <li>Renewable energy systems<span>›</span></li>
    <li>Power/heating<span>›</span></li>
    <li>Survival products<span>›</span></li>
    <li>Outdoor vacations/living<span>›</span></li>
  </ul>
  <div class="side-label">Related Article</div>
  <div class="related-item"><div class="related-thumb" role="img" aria-label="Cabin in the woods" style="background:linear-gradient(#6d7c70,#2f3b33)"></div><div><div class="related-date">05-05-2022</div><div class="related-title">Some blog heading goes here</div></div></div>
  <div class="related-item"><div class="related-thumb" role="img" aria-label="Workshop woodwork" style="background:linear-gradient(#b8ab98,#7a5a3d)"></div><div><div class="related-date">05-05-2022</div><div class="related-title">Some blog heading goes here</div></div></div>
  <div class="related-item"><div class="related-thumb" role="img" aria-label="Timber frame build" style="background:linear-gradient(#c9cdd0,#a88e6e)"></div><div><div class="related-date">05-05-2022</div><div class="related-title">Some blog heading goes here</div></div></div>
</aside>

<footer class="abs site-footer">
  <div class="abs footer-brand"><span class="brand-mark"></span>Ridgepine Haven</div>

  <div class="abs footer-col" style="left:380px">
    <div class="footer-heading">Quick Links</div>
    <ul class="footer-links"><li>About</li><li>Service</li><li>Blog</li><li>Consulting</li><li>Store</li><li>Contact Us</li></ul>
  </div>

  <div class="abs footer-col" style="left:586px">
    <div class="footer-heading">Contact Us</div>
    <div class="contact-line"><svg width="10" height="12" viewBox="0 0 10 12"><path d="M5 0a4 4 0 0 1 4 4c0 3-4 8-4 8S1 7 1 4a4 4 0 0 1 4-4z" fill="#ccc"/></svg>some goes address here</div>
    <div class="contact-line"><svg width="10" height="10" viewBox="0 0 10 10"><path d="M2 0l2 2-1 2a6 6 0 0 0 3 3l2-1 2 2-2 2C4 10 0 6 0 2z" fill="#ccc"/></svg>+1 (555) 014-2230</div>
    <div class="contact-line"><svg width="12" height="9" viewBox="0 0 12 9"><rect x=".5" y=".5" width="11" height="8" fill="none" stroke="#ccc"/><path d="M.5.5L6 5l5.5-4.5" fill="none" stroke="#ccc"/></svg>info@ridgepinehaven.com</div>
    <div class="social-row"><span class="social-dot"></span><span class="social-dot"></span><span class="social-dot"></span><span class="social-dot"></span></div>
  </div>

  <div class="abs footer-col" style="left:860px">
    <div class="footer-heading">Newsletter</div>
    <p class="newsletter-note">Be the first to know about new cabins, guides, and promotions.</p>
    <div class="newsletter-form"><div class="newsletter-input">Enter your email</div><div class="newsletter-btn"><svg width="12" height="10" viewBox="0 0 12 10"><path d="M0 5h10M6 1l4 4-4 4" fill="none" stroke="#fff" stroke-width="1.5"/></svg></div></div>
  </div>

  <div class="abs copyright">©Copyright 2022 RidgepineHaven | All Rights Reserved</div>
  <div class="abs to-top"><svg width="10" height="8" viewBox="0 0 10 8"><path d="M1 7l4-5 4 5" fill="none" stroke="#ccc" stroke-width="1.5"/></svg></div>
</footer>

</body>
</html>
```